Quarlwick Builders Business Cards

I want to use the logo and make an unique business card that shows the textured Logo with brick and builings. I want to be able to stand out when I pass out business cards.

```html
<!DOCTYPE html>
<html lang="en">
<head>
<meta charset="utf-8">
<title>Quarlwick Builders Business Cards</title>
<link href="https://fonts.googleapis.com/css2?family=Montserrat:wght@500;700;800&family=Oswald:wght@500&display=swap" rel="stylesheet">
<style>
  :root{
    --stage:#2b2b2b;
    --brick:#8b3f22;
    --brick-dark:#6f3019;
    --brick-light:#9a4a2a;
    --panel-black:#050505;
    --ink-white:#ffffff;
    --art-warm:#c8552f;
    --art-deep:#5a2416;
    --art-stone:#a58a78;
  }
  *{box-sizing:border-box;margin:0;padding:0}
  html,body{width:1200px;height:800px;overflow:hidden;background:var(--stage)}
  .stage{position:relative;width:1200px;height:800px}
  .card{position:absolute;left:320px;width:560px;height:320px;border-radius:18px;overflow:hidden;
        box-shadow:0 10px 30px rgba(0,0,0,.45)}
  .card--back{top:60px;display:flex}
  .card--front{top:420px}
  .brick-surface{background:linear-gradient(135deg,var(--brick-light),var(--brick) 50%,var(--brick-dark))}

  .brand-panel{width:44%;background:var(--panel-black);display:flex;flex-direction:column;align-items:center;justify-content:center;gap:14px;padding:20px}
  .contact-panel{flex:1;padding:34px 28px 28px 30px;color:var(--ink-white);font-family:"Montserrat",sans-serif}

  .logo-art{border-radius:10px;background:radial-gradient(ellipse at 50% 70%,var(--art-warm),var(--art-deep) 75%);display:flex;align-items:center;justify-content:center}
  .brand-panel .logo-art{width:200px;height:150px}
  .card--front .logo-art{width:300px;height:180px;margin:0 auto}
  .brand-name{font-family:"Montserrat",sans-serif;font-weight:800;color:var(--ink-white);letter-spacing:1px;text-align:center;line-height:1.1}
  .brand-panel .brand-name{font-size:17px}
  .card--front .brand-name{font-size:26px}

  .services{font-family:"Oswald",sans-serif;font-weight:500;color:var(--ink-white);white-space:nowrap;text-align:center}
  .brand-panel .services{font-size:12.5px}
  .card--front .services{font-size:22px;margin-top:22px}

  .person{border-left:4px solid var(--ink-white);padding-left:10px;margin-bottom:18px}
  .person-name{font-size:26px;font-weight:800;letter-spacing:.5px}
  .person-title{font-size:14px;font-weight:500}
  .contact-list{list-style:none;display:flex;flex-direction:column;gap:7px;font-size:14px;font-weight:500}
  .contact-list li{display:flex;align-items:center;gap:10px}
  .contact-list svg{width:15px;height:15px;flex:none}
  .address{margin-top:16px;font-size:14px;font-weight:500;line-height:1.35}

  .card--front{display:flex;flex-direction:column;justify-content:center;align-items:center;padding:22px}
  .front-art{position:relative}
  .front-art .brand-name{position:absolute;left:0;right:0;top:50%;transform:translateY(-50%)}
  .brand-panel .logo-art .brand-name{font-size:18px}
</style>
</head>
<body>
<main class="stage">

  <section class="card card--back">
    <div class="brand-panel">
      <div class="logo-art" role="img" aria-label="Illustration of red brick wall, city buildings and mason's tools">
        <span class="brand-name">QUARLWICK<br>BUILDERS</span>
      </div>
      <p class="services">Patios · Sidewalks · Retaining Walls · Foundations</p>
    </div>
    <div class="contact-panel brick-surface" role="img" aria-label="Red brick wall texture">
      <div class="person">
        <h1 class="person-name">DELIA MARSH</h1>
        <p class="person-title">Founder &amp; CEO</p>
      </div>
      <ul class="contact-list">
        <li><svg viewBox="0 0 16 16" fill="#fff"><path d="M4 1l3 3-2 2c1 2 3 4 5 5l2-2 3 3-2 3C7 15 1 9 1 3z"/></svg>012-555-014-372</li>
        <li><svg viewBox="0 0 16 16" fill="#fff"><path d="M1 6c0-3 14-3 14 0v1h-4V5H5v2H1zM3 8h10l1 6H2z"/></svg>044-555-208-614</li>
        <li><svg viewBox="0 0 16 16" fill="#fff"><path d="M1 8L15 1 11 15 8 9z"/></svg>info@quarlwick.com</li>
        <li><svg viewBox="0 0 16 16" fill="none" stroke="#fff" stroke-width="1.6"><circle cx="8" cy="8" r="6.5"/><path d="M1.5 8h13M8 1.5c-3 3-3 10 0 13M8 1.5c3 3 3 10 0 13"/></svg>www.quarlwickbuild.com</li>
      </ul>
      <p class="address">4417 Harrow Bay Pkwy 22-B,<br>FL 32090</p>
    </div>
  </section>

  <section class="card card--front brick-surface">
    <div class="front-art">
      <div class="logo-art" role="img" aria-label="Illustration of red brick wall, city buildings, trowel, hammer and level">
        <span class="brand-name">QUARLWICK BUILDERS</span>
      </div>
    </div>
    <p class="services">Patios - Sidewalks - Retaining Walls - Foundations</p>
  </section>

</main>
</body>
</html>
```